Sales Presentation Powerpoint

This project is to design a sales presentation for a new service/product for hotels.
The product is called snug stay and is a tablet pc that we propose to install in hotel rooms free of charge to hotels. The system has information about the hotel, room service menus, entertainment such as games, web browser, and other functions.
Marketing material has already been designed and the sell sheet that was recently completed is attached for your use.

Additionally, you will need to visit www.snugstaypad.example to see a demo of the product.

PRESENTATION REQUIRMENTS
General requirements – We will select the presentation that is the most visually crisp and stunning, stays within our already established visual themes, and includes multimedia. Interactivity and movement is a big plus if you can incorporate it into the presentation. We will be recording voiceover work on the presentation after it is made so you can plan around that thought.

PRESENTATION FLOW
1. General introduction to the product and what it is (info found on the sell sheet or you can contact me for more details if needed.
2. advantages of the product. Info found on the sell sheet or you can contact me for more details. Each of the main points on the sell sheet need to be a separate slide though so we can speak to it.
3. walkthrough of the product. I would like an animation, screen shots, or something similar to give the view the chance to experience and see the software. The demo at www.snugstaypad.example is the best place to go for that.

Recommendation for design:
Can we have the presentation be framed in a tablet window. to clarify, the border around the presentation is a tablet pc and the presentation appears inside of that.

Tools:
please feel free to use any software. does not need to be powerpoint. if you feel comfortable with solutions such as slidora, deckwave, or any other system you may use that.
Updates

Target Market(s)

presentation is for potential customers

Industry/Entity Type

Entertainment

Requirements
Must have
• visually crisp, sharp, and stunning
adheres to already established style from sell sheet and website.
multimedia encorporation a big plus.

```html
<!DOCTYPE html>
<html lang="en">
<head>
<meta charset="utf-8">
<title>Snug Stay – Sales Presentation Slides</title>
<link rel="stylesheet" href="https://fonts.googleapis.com/css2?family=Jost:wght@700;800&family=Carlito:wght@400;700&family=Tinos:wght@400;700&display=swap">
<style>
:root{
  --bg:#ffffff;
  --panel-light:#f6f6f6;
  --panel-dark:#c9c9c9;
  --red:#b5161b;
  --red-dark:#7a0b0e;
  --accent-red:#c8141b;
  --ink:#111111;
  --device:#111111;
  --device-edge:#3a3a3a;
  --icon:#8a8a8a;
  --gold:#d2a545;
  --wood-light:#b07a3c;
  --wood-dark:#5a3515;
  --demo-black:#050505;
  --orange:#e2621c;
  --yellow:#d9c21c;
  --green:#3f8a24;
  --blue:#1c8fe0;
}
*{box-sizing:border-box;margin:0;padding:0}
html,body{width:1200px;height:879px;overflow:hidden;background:var(--bg)}
body{position:relative;font-family:"Carlito",Calibri,sans-serif;color:var(--ink)}

.slide{position:absolute;width:576px;height:422px;overflow:hidden;
  background:radial-gradient(ellipse at 50% 35%,var(--panel-light) 0%,#e4e4e4 55%,var(--panel-dark) 100%);
  box-shadow:0 1px 4px rgba(0,0,0,.35)}
.slide--intro{left:22px;top:12px}
.slide--solution{left:610px;top:12px}
.slide--demo-welcome{left:25px;top:446px}
.slide--demo-signup{left:612px;top:446px}

.tablet-shadow{position:absolute;left:80px;top:360px;width:410px;height:40px;border-radius:50%;
  background:radial-gradient(ellipse at center,rgba(0,0,0,.45) 0%,rgba(0,0,0,0) 70%)}
.tablet{position:absolute;left:66px;top:42px;width:432px;height:334px;border-radius:42px;
  background:linear-gradient(180deg,#2b2b2b 0%,var(--device) 40%,#000 100%);
  box-shadow:inset 0 0 0 2px var(--device-edge),0 4px 10px rgba(0,0,0,.4)}
.tablet-controls{position:absolute;left:8px;top:118px;display:flex;flex-direction:column;gap:20px}
.tablet-controls svg{width:14px;height:14px;stroke:var(--icon);fill:none;stroke-width:1.4}

.screen{position:absolute;left:30px;top:26px;width:374px;height:272px;background:#fff;overflow:hidden}
.screen__title{height:62px;display:flex;align-items:center;padding-left:6px;
  background:linear-gradient(180deg,#c41d22 0%,var(--red) 45%,var(--red-dark) 100%);
  font-family:"Jost",Futura,sans-serif;font-weight:800;font-size:23px;letter-spacing:.2px;color:#fff;
  text-shadow:1px 2px 2px rgba(0,0,0,.55)}

.bullets{padding:10px 10px 0 8px}
.bullets__head{display:flex;align-items:center;gap:8px;color:var(--accent-red);font-weight:700;font-size:15.5px}
.bullets__head small{font-size:11px}
.bullets__dot{width:10px;height:10px;border:1.5px solid var(--accent-red);border-radius:50%;position:relative;flex:none}
.bullets__dot::after{content:"";position:absolute;left:2px;top:2px;width:3px;height:3px;border-radius:50%;background:var(--accent-red)}
.bullets ul{list-style:none;margin:3px 0 0 24px}
.bullets li{position:relative;padding-left:18px;font-size:13.2px;line-height:17px;margin-bottom:3px}
.bullets li::before{content:"–";position:absolute;left:0;color:var(--accent-red)}

.question-mark{position:absolute;font-family:"Jost",sans-serif;font-weight:800;font-size:22px;color:var(--accent-red);
  text-shadow:1px 2px 2px rgba(0,0,0,.3)}
.gear{position:absolute;width:18px;height:18px;border-radius:50%;background:var(--accent-red);
  box-shadow:1px 2px 3px rgba(0,0,0,.3)}
.gear::after{content:"";position:absolute;left:6px;top:6px;width:6px;height:6px;border-radius:50%;background:#eee}

.brand{position:absolute;right:20px;bottom:20px;display:flex;align-items:center;gap:4px}
.brand__mark{width:12px;height:12px;border-radius:50%;background:var(--ink)}
.brand__name{font-size:8px;color:var(--ink)}
.brand__tag{position:absolute;left:16px;top:12px;font-size:5px;color:var(--ink);white-space:nowrap}

/* demo screens */
.demo{position:absolute;left:2px;top:66px;width:370px;height:204px;background:var(--demo-black);overflow:hidden;
  font-family:"Tinos","Times New Roman",serif;color:#fff}
.wood{position:absolute;left:0;width:100%;
  background:linear-gradient(180deg,var(--wood-light) 0%,#8a5a28 50%,var(--wood-dark) 100%)}
.wood--top{top:0;height:26px}
.wood--bottom{bottom:0;height:26px}

.welcome{position:absolute;left:0;right:0;top:34px;text-align:center}
.welcome__title{color:var(--gold);font-size:14px;line-height:15px;letter-spacing:1px}
.hotel-badge{display:inline-flex;align-items:center;gap:4px;background:#fff;color:var(--ink);padding:3px 7px;margin-top:1px;border:1px solid #999;line-height:1}
.hotel-badge__mark{width:7px;height:7px;border-radius:50%;background:var(--ink)}
.hotel-badge__name{font-size:10px;font-weight:700;letter-spacing:1px}
.hotel-badge__place{display:block;font-size:4.5px;letter-spacing:.3px;margin-top:2px}
.welcome__tagline{color:var(--gold);font-size:6px;line-height:7px;margin-top:5px}
.flags{display:flex;justify-content:center;gap:10px;margin-top:7px}
.flag{width:18px;height:12px;display:flex}
.flag--us{background:repeating-linear-gradient(180deg,#c21d2a 0 2px,#fff 2px 4px)}
.flag--mx{background:linear-gradient(90deg,#1a7a3a 33%,#fff 33% 66%,#c21d2a 66%)}
.flag--it{background:linear-gradient(90deg,#1a8a3a 33%,#fff 33% 66%,#c21d2a 66%)}
.flag--ru{background:linear-gradient(180deg,#fff 33%,#2a50b0 33% 66%,#c21d2a 66%)}
.welcome__lang{color:var(--gold);font-size:6px;line-height:7px;margin-top:6px}
.guest-buttons{position:absolute;top:140px;left:0;right:0;display:flex;justify-content:center;gap:62px}
.guest-btn{width:64px;height:18px;border-radius:9px;font-family:"Carlito",sans-serif;font-weight:700;font-size:6px;
  display:flex;align-items:center;justify-content:center;color:#fff;box-shadow:inset 0 1px 1px rgba(255,255,255,.5)}
.guest-btn--returning{background:linear-gradient(180deg,#e3bb6a,#a67a2d)}
.guest-btn--new{background:linear-gradient(180deg,#6db34a,var(--green))}
.pointer{position:absolute;left:246px;top:150px;width:14px;height:16px}

.signup-badge{position:absolute;left:160px;top:2px;display:flex;align-items:center;gap:3px;background:#e6e6e6;color:var(--ink);
  padding:3px 6px;border-radius:3px}
.signup-badge .hotel-badge__name{font-size:8px}
.signup-note{position:absolute;left:0;right:0;text-align:center;font-size:5px}
.signup-note--1{top:32px}
.signup-note--2{top:46px}
.form-heading{position:absolute;left:40px;top:68px;width:280px;color:var(--orange);font-family:"Carlito",sans-serif;font-size:10px;
  padding-bottom:4px;border-bottom:1.5px solid var(--yellow)}
.form-row{position:absolute;left:40px;display:flex;align-items:center;gap:6px;font-family:"Carlito",sans-serif;font-size:5.5px}
.form-row label{width:44px;text-align:right}
.form-row input,.form-row .select{height:9px;border:none;background:#fff;font-family:"Courier New",monospace;font-size:6px;color:#000;padding-left:2px}
.scrollbar{position:absolute;right:4px;top:30px;width:6px;height:150px;background:#ddd}
.home-btn{position:absolute;left:166px;bottom:5px;width:34px;height:14px;border-radius:7px;background:linear-gradient(180deg,#555,#111);
  font-family:"Carlito",sans-serif;font-size:6px;display:flex;align-items:center;justify-content:center;border:1px solid #888}
.demo-warning{position:absolute;left:206px;bottom:9px;font-size:5px;color:#111;font-weight:700}
.login-btn{position:absolute;right:4px;bottom:5px;width:46px;height:12px;background:var(--blue);font-family:"Carlito",sans-serif;font-size:4.5px;
  display:flex;align-items:center;justify-content:center}
</style>
</head>
<body>

<section class="slide slide--intro">
  <span class="question-mark" style="left:32px;top:92px">?</span>
  <span class="question-mark" style="left:23px;top:200px">?</span>
  <span class="question-mark" style="left:25px;top:320px">?</span>
  <span class="question-mark" style="left:525px;top:101px">?</span>
  <span class="question-mark" style="left:525px;top:184px">?</span>
  <span class="question-mark" style="left:525px;top:278px">?</span>
  <div class="tablet-shadow"></div>
  <div class="tablet">
    <div class="tablet-controls">
      <svg viewBox="0 0 14 14"><path d="M2 5h6V2l5 5-5 5V9H2z"/></svg>
      <svg viewBox="0 0 14 14"><path d="M3 1h8M3 13h8M4 1c0 4 6 4 6 6s-6 2-6 6M10 1c0 4-6 4-6 6s6 2 6 6"/></svg>
      <svg viewBox="0 0 14 14"><circle cx="8" cy="6" r="4"/><path d="M5 9l-4 4"/></svg>
    </div>
    <div class="screen">
      <h1 class="screen__title">WELCOME TO SNUG STAY</h1>
      <div class="bullets">
        <p class="bullets__head"><span class="bullets__dot"></span><span>What is SNUG STAY<small>?</small></span></p>
        <ul>
          <li>Is a revolutionary re-design of the way a hospitality establishment connects with the costumer</li>
          <li>Lorem ipsum dolor sit amet, consectetur adipiscing elit. In nec urna sit amet nisi luctus dignissim in facilisis turpis.</li>
          <li>Nullam in libero eget odio fermentum ornare ac vitae turpis.</li>
          <li>Aliquam erat volutpat. Integer sagittis suscipit</li>
        </ul>
      </div>
    </div>
  </div>
  <div class="brand"><span class="brand__mark"></span><span class="brand__name">Snug Stay</span><span class="brand__tag">Hotel tablet solutions</span></div>
</section>

<section class="slide slide--solution">
  <span class="gear" role="img" aria-label="gear icon" style="left:14px;top:76px"></span>
  <span class="gear" role="img" aria-label="gear icon" style="left:26px;top:136px"></span>
  <span class="gear" role="img" aria-label="gear icon" style="left:13px;top:196px"></span>
  <span class="gear" role="img" aria-label="gear icon" style="left:27px;top:268px"></span>
  <span class="gear" role="img" aria-label="gear icon" style="left:13px;top:333px"></span>
  <span class="gear" role="img" aria-label="gear icon" style="left:500px;top:22px"></span>
  <span class="gear" role="img" aria-label="gear icon" style="left:515px;top:77px"></span>
  <span class="gear" role="img" aria-label="gear icon" style="left:515px;top:140px"></span>
  <span class="gear" role="img" aria-label="gear icon" style="left:515px;top:193px"></span>
  <span class="gear" role="img" aria-label="gear icon" style="left:511px;top:250px"></span>
  <span class="gear" role="img" aria-label="gear icon" style="left:527px;top:317px"></span>
  <div class="tablet-shadow"></div>
  <div class="tablet">
    <div class="tablet-controls">
      <svg viewBox="0 0 14 14"><path d="M2 5h6V2l5 5-5 5V9H2z"/></svg>
      <svg viewBox="0 0 14 14"><path d="M3 1h8M3 13h8M4 1c0 4 6 4 6 6s-6 2-6 6M10 1c0 4-6 4-6 6s6 2 6 6"/></svg>
      <svg viewBox="0 0 14 14"><circle cx="8" cy="6" r="4"/><path d="M5 9l-4 4"/></svg>
    </div>
    <div class="screen">
      <h1 class="screen__title">WELCOME TO SNUG STAY</h1>
      <div class="bullets">
        <p class="bullets__head"><span class="bullets__dot"></span><span>Complete Solution</span></p>
        <ul>
          <li>Aliquam libero ligula, laoreet non auctor in, porttitor in felis. Nulla facilisi.</li>
          <li>Sed non felis vitae eros ultrices pretium. Sed eu lectus metus, vel interdum dolor.</li>
          <li>Aenean eu vestibulum sapien. Ut eget turpis tellus. Nullam sed est et justo lobortis laoreet auctor in nibh.</li>
          <li>Mauris faucibus enim sed enim luctus ornare.</li>
        </ul>
      </div>
    </div>
  </div>
  <div class="brand"><span class="brand__mark"></span><span class="brand__name">Snug Stay</span><span class="brand__tag">Hotel tablet solutions</span></div>
</section>

<section class="slide slide--demo-welcome">
  <div class="tablet-shadow"></div>
  <div class="tablet">
    <div class="tablet-controls">
      <svg viewBox="0 0 14 14"><path d="M2 5h6V2l5 5-5 5V9H2z"/></svg>
      <svg viewBox="0 0 14 14"><path d="M3 1h8M3 13h8M4 1c0 4 6 4 6 6s-6 2-6 6M10 1c0 4-6 4-6 6s6 2 6 6"/></svg>
      <svg viewBox="0 0 14 14"><circle cx="8" cy="6" r="4"/><path d="M5 9l-4 4"/></svg>
    </div>
    <div class="screen">
      <h1 class="screen__title">PRODUCT DEMO</h1>
      <div class="demo">
        <div class="wood wood--top" role="img" aria-label="wood grain band"></div>
        <div class="welcome">
          <p class="welcome__title">WELCOME</p>
          <div class="hotel-badge"><span class="hotel-badge__mark"></span><span><span class="hotel-badge__name">ARDEN HOTEL</span><span class="hotel-badge__place">HARBOR / BAYSIDE / AIRPORT</span></span></div>
          <p class="welcome__tagline">The Hospitality Of Arden Hotels At Your Fingertips</p>
          <div class="flags"><span class="flag flag--us"></span><span class="flag flag--mx"></span><span class="flag flag--it"></span><span class="flag flag--ru"></span></div>
          <p class="welcome__lang">Language: English</p>
        </div>
        <div class="guest-buttons">
          <span class="guest-btn guest-btn--returning">Returning Guest</span>
          <span class="guest-btn guest-btn--new">New Guest</span>
        </div>
        <svg class="pointer" viewBox="0 0 14 16"><path d="M4 15V3a1.3 1.3 0 0 1 2.6 0v6l5 1.5c1 .3 1.4 1 1.2 2L12 15z" fill="#fff" stroke="#000" stroke-width=".8"/></svg>
        <div class="wood wood--bottom" role="img" aria-label="wood grain band"></div>
      </div>
    </div>
  </div>
  <div class="brand"><span class="brand__mark"></span><span class="brand__name">Snug Stay</span><span class="brand__tag">Hotel tablet solutions</span></div>
</section>

<section class="slide slide--demo-signup">
  <div class="tablet-shadow"></div>
  <div class="tablet">
    <div class="tablet-controls">
      <svg viewBox="0 0 14 14"><path d="M2 5h6V2l5 5-5 5V9H2z"/></svg>
      <svg viewBox="0 0 14 14"><path d="M3 1h8M3 13h8M4 1c0 4 6 4 6 6s-6 2-6 6M10 1c0 4-6 4-6 6s6 2 6 6"/></svg>
      <svg viewBox="0 0 14 14"><circle cx="8" cy="6" r="4"/><path d="M5 9l-4 4"/></svg>
    </div>
    <div class="screen">
      <h1 class="screen__title">PRODUCT DEMO</h1>
      <div class="demo">
        <div class="wood wood--top" role="img" aria-label="wood grain band"></div>
        <div class="signup-badge"><span class="hotel-badge__mark"></span><span class="hotel-badge__name">ARDEN HOTELS</span></div>
        <p class="signup-note signup-note--1">Please create your tablet account to access hotel information, dining menus, entertainment content, and the web browser</p>
        <p class="signup-note signup-note--2">You will only need to create a tablet account once to enjoy access at every Arden Hotels property every time you stay with us</p>
        <p class="form-heading">FULL NAME</p>
        <div class="form-row" style="top:94px"><label>Title</label><span class="select" style="width:26px">Mr ▾</span></div>
        <div class="form-row" style="top:108px"><label>First Name</label><input value="John" style="width:112px"></div>
        <div class="form-row" style="top:122px"><label>Last Name</label><input value="Smith" style="width:112px"></div>
        <div class="form-row" style="top:138px"><label>Suffix</label><input value="" style="width:26px"></div>
        <div class="scrollbar"></div>
        <div class="wood wood--bottom" role="img" aria-label="wood grain band"></div>
        <span class="home-btn">HOME</span>
        <span class="demo-warning">Please do not create an account in demo</span>
        <span class="login-btn">Click arrow to log in</span>
      </div>
    </div>
  </div>
  <div class="brand"><span class="brand__mark"></span><span class="brand__name">Snug Stay</span><span class="brand__tag">Hotel tablet solutions</span></div>
</section>

</body>
</html>
```